Event Website Design

We need a new website design for an events driven website. The domain for this site is http://brackmoorhalls.co.uk. The site is up and running but needs a new fresh, modern look.
I've attached a Balamiq Mockup for the layout of the home page. Also attached is a png of the logo.
Key colours for the site are 0f7e6a, 35bde, d57835 & 373737.
Font to use is Proxima Nova
Width of the site should be 1200px
The design should be contemporary with minimal clutter.
Websites to references are…
http://vantora.london/
http://www.thekrd.co.uk/
These are just guidelines, please feel free to use you own creative judgment.
The selected design file needs to be supplied as an editable PSD.
Updates
Reason: I've submitted 5 designs to the client, who will select the one they want. I will then choose that design. So please be patient as I'm waiting for a decision from my client.
Industry/Entity Type
Events
Number of Pages Required
1 page
Look and feel
Each slider illustrates characteristics of the customer's brand and the style your logo design should communicate.

```html
<!DOCTYPE html>
<html lang="en">
<head>
<meta charset="utf-8">
<title>Brackmoor Halls – Home</title>
<link href="https://fonts.googleapis.com/css2?family=Arimo:ital,wght@0,400;0,700;1,400;1,700&family=Roboto+Condensed:wght@400;700&display=swap" rel="stylesheet">
<style>
:root{
  --black:#000000;
  --white:#ffffff;
  --teal:#006e66;
  --teal-card:#0b5e59;
  --teal-btn:#0f7e6a;
  --ink:#111111;
  --social-a:#3b5aa0;
  --social-b:#c23a8a;
  --social-c:#3aa0e0;
  --logo-teal:#2aa6a6;
}
*{margin:0;padding:0;box-sizing:border-box}
html,body{width:1200px;height:2557px;overflow:hidden;background:var(--white);font-family:"Arimo",Arial,sans-serif;color:var(--ink)}
.page{position:relative;width:1200px;height:2557px}
.abs{position:absolute}

.site-header{left:0;top:0;width:1200px;height:159px;background:var(--black);color:var(--white)}
.brand{left:20px;top:44px;font-family:"Roboto Condensed",sans-serif;font-weight:700;font-size:32px;letter-spacing:1px;color:var(--white);display:flex;align-items:center;gap:10px}
.brand-mark{width:22px;height:22px;background:var(--logo-teal);flex:none}
.tagline{left:20px;top:119px;font-size:19px;font-weight:700;letter-spacing:-0.4px}
.utility{right:22px;top:12px;display:flex;gap:14px;font-size:20px;letter-spacing:-0.6px;font-family:"Roboto Condensed","Arimo",sans-serif}
.social{left:794px;top:53px;display:flex;gap:12px}
.social span{display:block;width:40px;height:40px;border-radius:7px}
.social .s1{background:var(--social-a)}
.social .s2{background:var(--social-b)}
.social .s3{background:var(--social-c);border-radius:50%}
.search{left:971px;top:59px;width:199px;height:29px;background:var(--white);border-radius:4px;color:#555;font-style:italic;font-size:20px;padding:3px 20px}
.phone{left:976px;top:110px;display:flex;align-items:center;gap:10px;font-size:23px;font-weight:700;font-style:italic}

.main-nav{left:0;top:159px;width:1200px;height:37px;display:flex;justify-content:space-between;align-items:center;padding:0 24px 0 52px;font-size:19px;letter-spacing:-0.4px;border-bottom:1px solid #bbb}

.hero{left:0;top:196px;width:1200px;height:443px;background:
  radial-gradient(ellipse 14% 16% at 44% 20%,rgba(255,240,200,.95),rgba(255,220,150,0) 100%),
  radial-gradient(ellipse 10% 10% at 36% 34%,rgba(255,230,180,.8),rgba(255,230,180,0) 100%),
  radial-gradient(ellipse 8% 9% at 64% 62%,rgba(200,190,255,.8),rgba(200,190,255,0) 100%),
  radial-gradient(ellipse 40% 30% at 80% 25%,#e04a2a,rgba(224,74,42,0) 100%),
  radial-gradient(ellipse 40% 30% at 12% 20%,#e8602e,rgba(232,96,46,0) 100%),
  linear-gradient(180deg,#c8281e 0%,#e04a25 22%,#b01c18 45%,#5a1416 62%,#3a1d24 75%,#6a4a48 88%,#8a6a62 100%)}

.promo{top:673px;width:309px;height:266px;color:var(--white);background:
  radial-gradient(ellipse 30% 12% at 30% 46%,rgba(170,200,255,.7),rgba(170,200,255,0)),
  radial-gradient(ellipse 30% 12% at 75% 48%,rgba(150,190,255,.6),rgba(150,190,255,0)),
  radial-gradient(ellipse 10% 8% at 62% 42%,rgba(255,190,110,.85),rgba(255,190,110,0)),
  linear-gradient(180deg,#6a6e80 0%,#3e4262 18%,#2c3a86 40%,#1f3390 55%,#16204e 75%,#0c1430 100%)}
.promo-text{position:absolute;left:14px;top:170px;font-size:21px;line-height:26px}
.promo-actions{position:absolute;left:14px;top:225px;display:flex;gap:8px}
.btn{background:var(--teal-btn);color:var(--white);font-size:18px;padding:0 8px;border-radius:10px;line-height:23px}

.latest{left:70px;top:965px;width:1057px;height:312px;background:var(--teal)}
.latest-title{position:absolute;left:32px;top:12px;font-size:22px;font-weight:400;color:var(--ink)}
.latest-more{position:absolute;left:32px;top:44px;font-size:15px}
.news-card{position:absolute;top:84px;width:307px;height:218px;background:var(--teal-card);padding:0 24px}
.news-card h3{font-family:"Roboto Condensed",sans-serif;font-weight:700;font-size:25px;text-align:center;margin-top:14px;line-height:28px}
.news-card p{font-size:21px;line-height:25px;margin-top:0}

.feature-title{top:1314px;width:336px;text-align:center;font-family:"Roboto Condensed",sans-serif;font-weight:700;font-size:25px}
.feature-img{top:1352px;width:336px;height:220px}
.conf{background:
  radial-gradient(ellipse 28% 40% at 30% 62%,#1c2a55,rgba(28,42,85,0) 100%),
  radial-gradient(ellipse 14% 12% at 33% 20%,#c08a6a,rgba(192,138,106,0) 100%),
  radial-gradient(ellipse 40% 30% at 75% 50%,#d86a5a,rgba(216,106,90,0) 100%),
  radial-gradient(ellipse 30% 25% at 60% 70%,#e8a060,rgba(232,160,96,0) 100%),
  linear-gradient(180deg,#aeb6c6 0%,#9aa2b6 22%,#c07a78 45%,#a0606a 65%,#6a6e88 85%,#c8c8d0 100%)}
.party{background:
  radial-gradient(ellipse 16% 14% at 26% 22%,rgba(250,250,220,.95),rgba(250,250,220,0) 100%),
  radial-gradient(ellipse 30% 20% at 62% 72%,#e2c79a,rgba(226,199,154,0) 100%),
  radial-gradient(ellipse 20% 20% at 18% 48%,#7fc06a,rgba(127,192,106,0) 100%),
  radial-gradient(ellipse 30% 30% at 55% 35%,#7a5ab0,rgba(122,90,176,0) 100%),
  linear-gradient(180deg,#3a3060 0%,#2a2245 45%,#161426 75%,#0a0a12 100%)}

.sports{left:68px;top:1679px;width:1059px;height:222px;background:
  radial-gradient(ellipse 12% 22% at 55% 30%,#f2f2ee,rgba(242,242,238,0) 100%),
  radial-gradient(ellipse 16% 14% at 85% 62%,#e6e6e2,rgba(230,230,226,0) 100%),
  radial-gradient(ellipse 22% 40% at 32% 22%,#cdbb9a,rgba(205,187,154,0) 100%),
  radial-gradient(ellipse 18% 36% at 72% 22%,#cbb896,rgba(203,184,150,0) 100%),
  linear-gradient(180deg,#7c98a8 0%,#a4aaa6 30%,#b4ab90 48%,#8cae58 64%,#6a9a34 80%,#4a7a22 100%)}
.sports-label{position:absolute;left:343px;top:75px;width:351px;height:69px;background:rgba(60,60,60,0.55);display:flex;align-items:center;justify-content:center;font-family:"Roboto Condensed",sans-serif;font-weight:700;font-size:24px;color:#111}

.site-footer{left:0;top:1918px;width:1200px;height:309px;background:var(--black);color:var(--white)}
.address{position:absolute;left:72px;top:64px;font-family:"Roboto Condensed",sans-serif;font-weight:700;font-style:normal;font-size:26px;line-height:31px;text-transform:uppercase;letter-spacing:-0.3px}
.footer-links{position:absolute;top:66px;list-style:none;font-size:21px;line-height:25px;letter-spacing:-0.4px}
.footer-brand{position:absolute;left:918px;top:100px;font-family:"Roboto Condensed",sans-serif;font-weight:700;font-size:30px;line-height:32px;letter-spacing:1px;display:flex;align-items:center;gap:10px}
</style>
</head>
<body>
<div class="page">

<header class="site-header abs">
  <div class="brand abs"><span class="brand-mark"></span>BRACKMOOR HALLS</div>
  <div class="tagline abs">somerset's premiere entertaiment &amp; Sporting Centre</div>
  <nav class="utility abs"><span>Gift Voucher</span><span>Join Our Mailing List</span><span>Basket</span><span>Register</span><span>My Account</span></nav>
  <div class="social abs"><span class="s1"></span><span class="s2"></span><span class="s3"></span></div>
  <div class="search abs">Search</div>
  <div class="phone abs">
    <svg width="42" height="42" viewBox="0 0 24 24" aria-hidden="true"><path fill="#fff" d="M6.6 10.8a15.1 15.1 0 0 0 6.6 6.6l2.2-2.2a1 1 0 0 1 1-.25 11.4 11.4 0 0 0 3.6.57 1 1 0 0 1 1 1V20a1 1 0 0 1-1 1A17 17 0 0 1 3 4a1 1 0 0 1 1-1h3.5a1 1 0 0 1 1 1c0 1.25.2 2.45.57 3.57a1 1 0 0 1-.25 1z"/></svg>
    <span>01632 960 418</span>
  </div>
</header>

<nav class="main-nav abs">
  <span>What's On |</span><span>Conferencing &amp; Events |</span><span>Sports &amp; Leisure |</span><span>Lantern Theatre |</span><span>Plan Your Visit |</span><span>News |</span><span>Discover More |</span><span>Contact Us</span>
</nav>

<div class="hero abs" role="img" aria-label="Banqueting hall lit in red and orange with chandeliers and round dining tables"></div>

<article class="promo abs" style="left:95px" role="img" aria-label="Event hall with blue stage lighting">
  <div class="promo-text">LED Promote<br>Date : ( 7 mon )</div>
  <div class="promo-actions"><span class="btn">More</span><span class="btn">Book</span></div>
</article>
<article class="promo abs" style="left:445px" role="img" aria-label="Event hall with blue stage lighting">
  <div class="promo-text">LED Promote<br>Date : ( 7 mon )</div>
  <div class="promo-actions"><span class="btn">More</span><span class="btn">Book</span></div>
</article>
<article class="promo abs" style="left:795px" role="img" aria-label="Event hall with blue stage lighting">
  <div class="promo-text">LED Promote<br>Date : ( 7 mon )</div>
  <div class="promo-actions"><span class="btn">More</span><span class="btn">Book</span></div>
</article>

<section class="latest abs">
  <h2 class="latest-title">Latest From Brackmoor Halls</h2>
  <div class="latest-more">Show More</div>
  <div class="news-card" style="left:39px"><h3>New Info</h3><p>Lorem Ipsum dolor sit amet , consectetur elit , sed do elusmod tempor incidudnt ut laboreet dolore magna aliqua .</p></div>
  <div class="news-card" style="left:375px"><h3>New Info</h3><p>Lorem Ipsum dolor sit amet , consectetur elit , sed do elusmod tempor incidudnt ut laboreet dolore magna aliqua .</p></div>
  <div class="news-card" style="left:711px"><h3>New Info</h3><p style="margin-top:40px">Lorem Ipsum dolor sit amet , consectetur elit , sed do elusmod tempor incidudnt ut laboreet dolore magna aliqua .</p></div>
</section>

<h2 class="feature-title abs" style="left:68px">Conference &amp; Event</h2>
<h2 class="feature-title abs" style="left:431px">Parties at Brackmoor Halls</h2>
<h2 class="feature-title abs" style="left:791px">Conference &amp; Event</h2>
<div class="feature-img conf abs" style="left:68px" role="img" aria-label="Speaker at a laptop addressing a conference audience"></div>
<div class="feature-img party abs" style="left:431px" role="img" aria-label="Tray of champagne glasses at an evening party"></div>
<div class="feature-img conf abs" style="left:791px" role="img" aria-label="Speaker at a laptop addressing a conference audience"></div>

<section class="sports abs" role="img" aria-label="Golfer putting on a green">
  <div class="sports-label">Sports &amp; Leasure</div>
</section>

<footer class="site-footer abs">
  <address class="address">Brackmoor Events Venue<br>Harrow Lane<br>Brackmoor<br>Somerset<br>TA9 4QX</address>
  <ul class="footer-links" style="left:479px"><li>What's On</li><li>Conferencing &amp; Events</li><li>Sports &amp; Leisure</li><li>Lantern Theatre</li></ul>
  <ul class="footer-links" style="left:716px"><li>Plan Your Visit</li><li>News</li><li>Discover More</li><li>Contact Us</li></ul>
  <div class="footer-brand"><span class="brand-mark"></span><span>BRACKMOOR<br>HALLS</span></div>
</footer>

</div>
</body>
</html>
```